Pastured Free Range Egg farm needs carton label

We have recently updated our logo, and are looking to incorporate the new logo into a new design for our dozen size egg cartons. (New logo has been included in the uploads - there are several file formats available, so let me know if you need a different file format for the logo.)
We are a company that is focused on ethical farming, and the welfare of our hens. We are a small, niche farm, run by a husband and wife and 3 children.
I have included a photo of our farm and the trailers we use for our hens so that you can see the type of farming methods we use.
We would like to keep the label relaxed, to reflect the small family business.
We would like the use of green colours to represent the "pastured" aspect of our egg farming. We want the label to represent our better farming practices.
We have included a graphic of our current label which we like the feel and style of.
We have also included a graphic of the dieline that must be used so we can submit the design to the printing company. (we do not need a space for a barcode on our label)
______________
Things that must be included legally on the label:
* The words "12 Pastured Free Range Eggs",
*Nutrition label panel as pictured in the current label graphic
* Weight options as pictured in the current label the words "Min Total Mass" must be used and have a selection for weights of 600gm, 700gm and 800gm
* Chicken stocking density must be prominent to show our care for the hens the words "150 chickens per hectare" must be used
* A best before section where we can stamp a date
* A product of Australia logo
* The words "Commercial reuse of this carton prohibited" on the back of the carton
* A "please recycle" logo on the back of the carton
* Farm details on the back of the carton:
Marrow Farm
T & K Marrow
82 Pellam Rd
Broadford VIC 3658
Ph: 0438 716 502
I would like some information on our farming practices like what is pictured on the original label:
" Our hens are housed in mobile trailers that are moved to fresh pasture regularly on our farm in Broadford, Victoria.
The hens have access to the outdoors 24 hours a day. They have plenty of room to flap their wings, and to scratch and forage for bugs.
Our hens are happy and healthy, help to sustain our land, and lay us these delicious eggs!"
People wanting ethical sustainable produce

```html
<!DOCTYPE html>
<html lang="en">
<head>
<meta charset="utf-8">
<title>Marrow Farm – Egg Carton Label</title>
<link rel="stylesheet" href="https://fonts.googleapis.com/css2?family=Fira+Sans:wght@700;800&family=Open+Sans:wght@400;600;700&family=Oswald:wght@300&family=Great+Vibes&display=swap">
<style>
  :root {
    --pasture: #00a04b;
    --pasture-deep: #008f45;
    --soil: #b35c00;
    --cream: #ffffff;
    --ink: #111111;
    --dieline: #d4267f;
    --table-green: #a8d88c;
  }
  * { box-sizing: border-box; margin: 0; padding: 0; }
  html, body { width: 1200px; height: 1200px; overflow: hidden; background: var(--cream); }
  .carton { position: relative; width: 1200px; height: 1200px; font-family: "Open Sans", sans-serif; }

  .panel { position: absolute; background: var(--pasture); border: 1px solid var(--dieline); overflow: hidden; }

  /* back flap (printed upside down) */
  .panel-back {
    left: 112px; top: 229px; width: 961px; height: 136px; z-index: 2;
    transform: rotate(180deg);
    border-radius: 0 0 18px 18px; border-top: none; border-bottom: 1px solid var(--dieline);
  }
  .panel-back > * { position: absolute; }
  .divider { width: 1px; background: rgba(0,0,0,.35); }

  .nutrition { right: 64px; bottom: 12px; width: 207px; height: 88px; background: #fff; padding: 2px; font-size: 5.2px; line-height: 1.15; color: var(--ink); }
  .nutrition h4 { font-size: 6.5px; font-weight: 700; }
  .nutrition table { width: 100%; border-collapse: collapse; margin-top: 1px; }
  .nutrition td, .nutrition th { border: 0.5px solid #6aa86a; padding: 0 2px; text-align: left; font-weight: 400; height: 8px; }
  .nutrition tr:nth-child(odd) td { background: var(--table-green); }
  .pack-sizes { right: 285px; bottom: 49px; width: 76px; height: 52px; background: #fff; border: 1px solid var(--table-green); padding: 2px; font-size: 5px; line-height: 1.3; color: var(--ink); }

  .reuse { right: 405px; bottom: 62px; width: 130px; font-size: 10px; line-height: 1.3; color: var(--cream); white-space: nowrap; }
  .recycle-label { right: 412px; bottom: 18px; width: 100px; font-size: 10px; letter-spacing: 1.5px; color: var(--cream); white-space: nowrap; }
  .recycle-icon { right: 523px; bottom: 12px; width: 22px; height: 22px; border-radius: 50%; border: 2px solid var(--cream); }
  .farm-address { right: 559px; bottom: 12px; width: 95px; font-size: 10px; line-height: 17px; color: var(--cream); white-space: nowrap; }
  .origin-badge { right: 688px; bottom: 12px; width: 54px; height: 86px; background: var(--cream); border-radius: 4px; }
  .back-brand { right: 790px; bottom: 40px; width: 115px; text-align: center; font-family: "Fira Sans", sans-serif; font-weight: 700; font-size: 18px; color: var(--cream); white-space: nowrap; }

  /* front lid */
  .panel-front { left: 68px; top: 364px; width: 1049px; height: 300px; border-radius: 44px; z-index: 1; }
  .panel-front > * { position: absolute; }
  .scene-art { left: 47px; top: 2px; width: 285px; height: 295px; background: linear-gradient(160deg, #1f5a2a 0%, #2e7d3a 45%, #8a5a22 100%); border-radius: 6px; opacity: .9; }
  .best-before { right: 554px; top: 12px; font-size: 11px; font-weight: 600; letter-spacing: 1px; color: var(--ink); }
  .happy-hens { right: 554px; top: 30px; font-family: "Great Vibes", cursive; font-size: 25px; color: var(--cream); white-space: nowrap; }
  .farm-story { right: 554px; top: 70px; width: 140px; text-align: right; font-size: 8.6px; line-height: 11.9px; color: var(--ink); }
  .story-rule { left: 506px; top: 70px; width: 1px; height: 140px; background: rgba(0,0,0,.45); }
  .density-figure { left: 518px; top: 56px; font-family: "Oswald", sans-serif; font-weight: 300; font-size: 74px; line-height: 1; color: var(--cream); }
  .density-label { left: 520px; top: 134px; font-size: 9px; font-weight: 700; letter-spacing: .4px; color: var(--ink); white-space: nowrap; }
  .front-brand { left: 690px; top: 172px; width: 290px; text-align: center; font-family: "Fira Sans", sans-serif; font-weight: 700; font-size: 42px; line-height: 1.2; color: var(--cream); white-space: nowrap; }
  .brand-dot { left: 805px; top: 60px; width: 60px; height: 60px; border-radius: 50%; background: var(--cream); }
  .soil-band { left: 0; top: 0; width: 1049px; height: 300px; }
  .egg-title { font-family: "Fira Sans", sans-serif; font-weight: 800; color: var(--cream); white-space: nowrap; }
  .panel-front .egg-title { left: 557px; top: 236px; font-size: 34px; }

  /* base flap */
  .panel-base { left: 112px; top: 663px; width: 961px; height: 139px; border-radius: 0 0 18px 18px; border-top: none; z-index: 2; }
  .panel-base > * { position: absolute; }
  .fold-line { left: 0; width: 100%; height: 0; border-top: 1px dashed var(--dieline); opacity: .7; }
  .vent { width: 84px; height: 78px; top: 12px; border: 1px solid var(--dieline); border-radius: 8px; background: rgba(0,120,60,.55); z-index: 3; }
  .base-brand { left: 137px; top: 70px; width: 125px; text-align: center; font-family: "Fira Sans", sans-serif; font-weight: 700; font-size: 19px; color: var(--cream); white-space: nowrap; }
  .base-rule { top: 38px; width: 1px; height: 87px; background: rgba(0,0,0,.35); }
  .weights { left: 294px; top: 36px; list-style: none; }
  .weights li { display: flex; align-items: center; gap: 10px; height: 24px; font-size: 15px; color: var(--ink); }
  .weights li::before { content: ""; width: 22px; height: 15px; border-radius: 50%; background: var(--cream); box-shadow: inset 2px 1px 0 #c98a3a; }
  .min-mass { left: 295px; top: 112px; font-size: 11px; font-weight: 700; color: var(--ink); white-space: nowrap; }
  .panel-base .egg-title { left: 515px; top: 88px; font-size: 31px; }
</style>
</head>
<body>
<div class="carton">

  <section class="panel panel-back" aria-label="Back flap">
    <div class="nutrition">
      <h4>NUTRITION INFORMATION</h4>
      <div>Servings per pack: 6 · Serving size: 2 eggs</div>
      <table>
        <tr><th></th><th>Per serve</th><th>Per 100g</th></tr>
        <tr><td>Energy</td><td>536kJ</td><td>561kJ</td></tr>
        <tr><td>Protein</td><td>12.1g</td><td>12.6g</td></tr>
        <tr><td>Fat, total</td><td>9.1g</td><td>9.5g</td></tr>
        <tr><td>– saturated</td><td>2.9g</td><td>3.0g</td></tr>
        <tr><td>Carbohydrate</td><td>0.3g</td><td>0.3g</td></tr>
        <tr><td>Sodium</td><td>130mg</td><td>136mg</td></tr>
      </table>
    </div>
    <div class="pack-sizes">Pack sizes:<br>600g – 12 eggs<br>700g – 12 eggs<br>800g – 12 eggs<br>Average quantity per egg.</div>
    <span class="divider" style="right:383px;bottom:12px;height:88px"></span>
    <p class="reuse">Commercial reuse of<br>this carton prohibited</p>
    <span class="recycle-icon" aria-hidden="true"></span>
    <p class="recycle-label">PLEASE RECYCLE</p>
    <span class="divider" style="right:535px;bottom:12px;height:88px"></span>
    <address class="farm-address" style="font-style:normal">Marrow Farm<br>T &amp; K Marrow<br>82 Pellam Rd<br>Broadford VIC 3658<br>Ph: 0438 716 502</address>
    <span class="divider" style="right:664px;bottom:12px;height:88px"></span>
    <span class="origin-badge" aria-hidden="true"></span>
    <span class="divider" style="right:766px;bottom:12px;height:88px"></span>
    <p class="back-brand">Marrow Farm</p>
  </section>

  <section class="panel panel-front" aria-label="Front lid">
    <svg class="soil-band" viewBox="0 0 1049 300" aria-hidden="true">
      <path d="M222 300 Q600 226 1000 226 Q1049 240 1049 256 L1049 300 Z" fill="var(--soil)"/>
      <line x1="222" y1="287" x2="420" y2="287" stroke="#222" stroke-width="1.5"/>
      <ellipse cx="506" cy="254" rx="40" ry="29" fill="var(--cream)" stroke="var(--ink)" stroke-width="1.5"/>
      <text x="506" y="270" text-anchor="middle" font-family="Oswald, sans-serif" font-weight="300" font-size="46" fill="var(--pasture)">12</text>
    </svg>
    <div class="scene-art" role="img" aria-label="Sketch of hens foraging on pasture beneath trees, with a mobile hen trailer behind"></div>
    <p class="best-before">BEST BEFORE</p>
    <p class="happy-hens">Happy Hens</p>
    <p class="farm-story">"Our hens are housed in mobile trailers that are moved to fresh pasture regularly on our farm in Broadford, Victoria. The hens have access to the outdoors 24 hours a day. They have plenty of room to flap their wings, and to scratch and forage for bugs. Our hens are happy and healthy, help to sustain our land, and lay us these delicious eggs!"</p>
    <span class="story-rule"></span>
    <p class="density-figure">150</p>
    <p class="density-label">chickens per hectare</p>
    <span class="brand-dot" aria-hidden="true"></span>
    <p class="front-brand">Marrow Farm</p>
    <p class="egg-title">Pastured Free Range Eggs</p>
  </section>

  <section class="panel panel-base" aria-label="Base flap">
    <svg style="left:0;top:0;width:961px;height:139px" viewBox="0 0 961 139" aria-hidden="true">
      <path d="M460 139 L460 74 Q640 56 961 100 L961 139 Z" fill="var(--soil)"/>
      <ellipse cx="462" cy="78" rx="40" ry="29" fill="var(--cream)" stroke="var(--ink)" stroke-width="1.5"/>
      <text x="462" y="94" text-anchor="middle" font-family="Oswald, sans-serif" font-weight="300" font-size="46" fill="var(--pasture)">12</text>
    </svg>
    <span class="fold-line" style="top:0"></span>
    <span class="fold-line" style="top:28px"></span>
    <span class="vent" style="left:47px"></span>
    <span class="vent" style="left:829px"></span>
    <p class="base-brand">Marrow Farm</p>
    <span class="base-rule" style="left:272px"></span>
    <ul class="weights"><li>600gm</li><li>700gm</li><li>800gm</li></ul>
    <p class="min-mass">Min Total Mass</p>
    <span class="base-rule" style="left:396px"></span>
    <p class="egg-title">Pastured Free Range Eggs</p>
  </section>

</div>
</body>
</html>
```